Lanternby Postcard Design

We need postcard designs for a new company based in Maryland called "Lanternby". We provide security guard services and we provide training for security guards. We would like two different cards, one for individuals who need training to become security guards through our training academy, and one targeted at businesses that are looking to hire security guards through our security agency. We are looking to project an image of strength, stability, trustworthiness and confidence.

Target Market(s)

Businesses that typically use security guard services, such as property management companies, restaurants, construction companies, etc.

Industry/Entity Type

Security

Requirements
Must have
• The card should be professional. It needs to grab the reader's attention right away.

```html
<!DOCTYPE html>
<html lang="en">
<head>
<meta charset="utf-8">
<title>Lanternby Security Postcard</title>
<link rel="stylesheet" href="https://fonts.googleapis.com/css2?family=Archivo+Black&family=Oswald:wght@600;700&display=swap">
<style>
  :root {
    --page: #e9ecef;
    --card: #ffffff;
    --ink: #111111;
    --red: #e2231a;
    --blue: #1f5fd6;
    --sky: #2fa8e8;
    --sky-pale: #dceefa;
    --steel: #9fb6c8;
    --banner-top: #3f8df0;
    --banner-bottom: #1c4fc4;
  }
  * { box-sizing: border-box; margin: 0; padding: 0; }
  html, body {
    width: 1200px; height: 779px; overflow: hidden;
    background: var(--page);
  }
  .postcard {
    position: absolute; left: 60px; top: 30px;
    width: 1080px; height: 720px;
    background: var(--card);
    overflow: hidden;
    box-shadow: 0 4px 18px rgba(0,0,0,.18);
  }
  .skyline {
    position: absolute; left: 0; bottom: 0; width: 100%; height: 60%;
    background: linear-gradient(180deg, rgba(255,255,255,0) 0%, var(--sky-pale) 55%, var(--steel) 100%);
  }
  .guard-photo {
    position: absolute; left: 0; top: 0; width: 420px; height: 390px;
    background: linear-gradient(135deg, var(--sky-pale) 0%, #c9dcea 55%, #7fa3c0 100%);
  }
  .accent-band {
    position: absolute; left: 250px; top: 0; width: 130px; height: 150px;
    background: var(--sky);
  }
  .title {
    position: absolute; right: 30px; top: 22px;
    font-family: "Archivo Black", sans-serif;
    font-size: 92px; line-height: 1; letter-spacing: 1px;
    color: var(--ink);
    text-shadow: 3px 3px 0 #888;
  }
  .tagline {
    position: absolute; right: 60px; top: 128px;
    font-family: "Archivo Black", sans-serif;
    font-size: 30px; color: var(--red); letter-spacing: 1px;
  }
  .phone {
    position: absolute; left: 440px; top: 180px;
    display: flex; align-items: center; gap: 14px;
    font-family: "Archivo Black", sans-serif;
    font-size: 54px; color: var(--blue);
  }
  .website {
    position: absolute; left: 440px; top: 252px;
    font-family: "Archivo Black", sans-serif;
    font-size: 26px; color: var(--ink);
  }
  .services-banner {
    position: absolute; left: 330px; top: 305px; width: 500px; height: 62px;
    background: linear-gradient(180deg, var(--banner-top), var(--banner-bottom));
    display: flex; align-items: center; justify-content: center;
    font-family: "Oswald", sans-serif; font-weight: 700;
    font-size: 40px; color: var(--red); letter-spacing: 1px;
    text-shadow: 1px 1px 0 #fff;
  }
  .service-list {
    position: absolute; left: 40px; top: 390px;
    list-style: none;
    font-family: "Archivo Black", sans-serif;
    font-size: 30px; line-height: 38px; color: var(--ink);
  }
  .service-list li { display: flex; align-items: center; gap: 12px; }
  .service-list li.bullet::before {
    content: ""; width: 0; height: 0;
    border-left: 16px solid var(--red);
    border-top: 9px solid transparent; border-bottom: 9px solid transparent;
  }
  .service-list li.cont { padding-left: 28px; }
  .brand-mark {
    position: absolute; right: 60px; bottom: 90px;
    display: flex; align-items: center; gap: 14px;
    font-family: "Archivo Black", sans-serif;
    font-size: 34px; color: var(--blue);
  }
  .brand-mark .dot {
    width: 34px; height: 34px; border-radius: 50%; background: var(--blue);
  }
</style>
</head>
<body>
  <main class="postcard">
    <div class="skyline" role="img" aria-label="Pale city skyline with glass towers"></div>
    <div class="accent-band"></div>
    <div class="guard-photo" role="img" aria-label="Photo of a uniformed security guard holding a baton"></div>

    <h1 class="title">LANTERNBY SECURITY</h1>
    <p class="tagline">SERVICES YOU CAN TRUST</p>

    <p class="phone">
      <svg width="48" height="44" viewBox="0 0 48 44" aria-hidden="true">
        <rect x="4" y="16" width="40" height="26" rx="5" fill="#1f5fd6"/>
        <path d="M2 14 Q24 0 46 14 L40 20 Q24 10 8 20 Z" fill="#1f5fd6"/>
        <circle cx="24" cy="29" r="7" fill="#fff"/>
      </svg>
      301-555-0142
    </p>
    <p class="website">www.lanternby-guard.com</p>

    <div class="services-banner">SECURITY GUARD SERVICES</div>

    <ul class="service-list">
      <li class="bullet">PRIVATE DETECTIVE</li>
      <li class="bullet">PERSONAL PROTECTION</li>
      <li class="bullet">BACKGROUND CHECKS</li>
      <li class="bullet">MARKED VEHICLE PATROLS</li>
      <li class="bullet">SECURITY CONSULTING AND</li>
      <li class="cont">RISK ASSESSMENT</li>
      <li class="bullet">ARMED AND UNARMED</li>
      <li class="cont">UNIFORMED SECURITY GUARDS</li>
    </ul>

    <div class="brand-mark"><span class="dot"></span>Lanternby</div>
  </main>
</body>
</html>
```